ultra-minimalist business card

front (black background, matte):

tarik b. hosseny
writer | photographer
get@tarikhosseny.com

back (white background, matte):

a picture speaks a thousand words;
a word draws a thousand pictures.

www.tarikhosseny.com

all text should be small (white or silver - as long as it shows against the black - on the front; black or gray - as long as it shows against the white - on the back).

feel free to get creative in terms of arrangement, alignment, and font type, but remember, the overall style is minimalist, so nothing too fancy, please.

thanks.

```html
<!DOCTYPE html>
<html lang="en">
<head>
<meta charset="utf-8">
<title>tarik b. hosseny — business card</title>
<link href="https://fonts.googleapis.com/css2?family=Quicksand:wght@400;500&display=swap" rel="stylesheet">
<style>
  :root {
    --backdrop: #cfcfcd;
    --card-front: #000000;
    --card-back: #ffffff;
    --ink-light: #ffffff;
    --ink-dark: #111111;
  }
  * { margin: 0; padding: 0; box-sizing: border-box; }
  html, body {
    width: 1200px;
    height: 1000px;
    overflow: hidden;
  }
  body {
    background: var(--backdrop);
    font-family: "Quicksand", sans-serif;
    position: relative;
  }
  .card {
    position: absolute;
    top: 374px;
    width: 441px;
    height: 252px;
  }
  .card-front {
    left: 119px;
    background: var(--card-front);
    color: var(--ink-light);
  }
  .card-back {
    left: 640px;
    background: var(--card-back);
    color: var(--ink-dark);
  }
  .name {
    position: absolute;
    top: 60px;
    width: 100%;
    text-align: center;
    font-size: 31px;
    font-weight: 400;
    letter-spacing: 0.5px;
  }
  .role {
    position: absolute;
    top: 104px;
    width: 100%;
    text-align: center;
    font-size: 19px;
    font-weight: 400;
    letter-spacing: 4.2px;
  }
  .contact {
    position: absolute;
    top: 195px;
    width: 100%;
    display: flex;
    justify-content: center;
    align-items: center;
    gap: 5px;
    font-size: 17.5px;
    font-weight: 400;
  }
  .contact svg { flex: none; }
  .motto {
    position: absolute;
    top: 52px;
    left: 0;
    width: 100%;
    font-size: 20.5px;
    line-height: 23.7px;
    font-weight: 400;
  }
  .motto-line {
    position: absolute;
    top: 0;
    white-space: nowrap;
  }
  .motto-left {
    right: 254px;
    text-align: right;
  }
  .motto-right {
    left: 255px;
    text-align: left;
  }
</style>
</head>
<body>
  <section class="card card-front" aria-label="Card front">
    <h1 class="name">tarik b. hosseny</h1>
    <p class="role">writer|photographer</p>
    <p class="contact">
      <svg width="20" height="14" viewBox="0 0 20 14" aria-hidden="true">
        <rect x="0.75" y="0.75" width="18.5" height="12.5" fill="none" stroke="currentColor" stroke-width="1.3"/>
        <path d="M0.75 0.75 L10 8 L19.25 0.75 M0.75 13.25 L7.5 6 M19.25 13.25 L12.5 6" fill="none" stroke="currentColor" stroke-width="1.3"/>
      </svg>
      <span>get@tarikhosseny.com</span>
    </p>
  </section>

  <section class="card card-back" aria-label="Card back">
    <div class="motto">
      <p class="motto-line motto-left">a picture<br>speaks<br>a thousand<br>words</p>
      <p class="motto-line motto-right">a word<br>draws<br>a thousand<br>pictures</p>
    </div>
    <p class="contact">
      <svg width="18" height="18" viewBox="0 0 18 18" aria-hidden="true">
        <g fill="none" stroke="currentColor" stroke-width="1.3">
          <circle cx="9" cy="9" r="8"/>
          <ellipse cx="9" cy="9" rx="3.5" ry="8"/>
          <path d="M1 9 H17 M2.5 4.8 H15.5 M2.5 13.2 H15.5"/>
        </g>
      </svg>
      <span>www.tarikhosseny.com</span>
    </p>
  </section>
</body>
</html>
```